Business Card Design Project

Need a business card designed for a horse racing/gambling centered company.
Company name is BrightQuill.com.au
Company colours are similar to those in the logo.
Something clean and modern , designer given liberty to be creative.
Incorporate the logo is preferred.
Single or Double Sided fine
Must include :
Name
Mobile Number
Email Address
Reason: Apologies, I have been traveling unexpectedly with business and just need the extra two days to reply and give feedback before making a decision.
Industry/Entity Type
Business

```html
<!DOCTYPE html>
<html lang="en">
<head>
<meta charset="utf-8">
<title>BrightQuill.com.au – Business Card</title>
<link rel="stylesheet" href="https://fonts.googleapis.com/css2?family=Open+Sans:wght@400;600;700&display=swap">
<style>
  :root {
    --page-bg: #ece9e4;
    --teal: #6aaea4;
    --teal-dark: #1f8377;
    --card-grey: #a3a5a8;
    --white: #ffffff;
    --shadow: rgba(0, 0, 0, 0.18);
  }
  * { box-sizing: border-box; margin: 0; padding: 0; }
  html, body {
    width: 1200px;
    height: 761px;
    overflow: hidden;
    background: var(--page-bg);
    font-family: "Open Sans", Arial, sans-serif;
  }
  .canvas {
    position: relative;
    width: 1200px;
    height: 761px;
    display: flex;
    align-items: center;
    justify-content: center;
    gap: 44px;
  }
  .card {
    position: relative;
    width: 430px;
    height: 430px;
    box-shadow: 0 6px 18px var(--shadow);
    overflow: hidden;
  }
  /* Front */
  .card--front {
    background: var(--teal);
    display: flex;
    align-items: center;
    justify-content: center;
  }
  .brand {
    display: flex;
    align-items: center;
    gap: 12px;
  }
  .brand__dot {
    width: 22px;
    height: 22px;
    border-radius: 50%;
    background: var(--white);
  }
  .brand__name {
    color: var(--white);
    font-weight: 700;
    font-size: 30px;
    letter-spacing: 0.5px;
  }
  /* Back */
  .card--back {
    background: var(--card-grey);
    color: var(--white);
  }
  .back__cap {
    position: absolute;
    top: 0;
    left: 0;
    width: 430px;
    height: 180px;
  }
  .contact {
    position: absolute;
    left: 0;
    right: 0;
    top: 200px;
    text-align: center;
  }
  .contact__name {
    font-size: 26px;
    font-weight: 600;
    margin-bottom: 22px;
  }
  .contact__lines {
    font-size: 19px;
    font-weight: 600;
    line-height: 1.22;
    font-style: normal;
  }
</style>
</head>
<body>
  <main class="canvas">
    <section class="card card--front" aria-label="Card front">
      <div class="brand">
        <span class="brand__dot"></span>
        <span class="brand__name">BrightQuill.com.au</span>
      </div>
    </section>

    <section class="card card--back" aria-label="Card back">
      <svg class="back__cap" viewBox="0 0 430 180" aria-hidden="true">
        <path d="M22 0 H408 C400 100 320 172 215 172 C110 172 30 100 22 0 Z" fill="var(--white)"/>
      </svg>
      <div class="contact">
        <p class="contact__name">Mara Ellison</p>
        <address class="contact__lines">
          0400 118 372<br>
          2710 /64 Harbour Lane<br>
          Sydney NSW 2000<br>
          mara@brightquill.com.au<br>
          www.brightquill.com.au
        </address>
      </div>
    </section>
  </main>
</body>
</html>
```